New bussiness card, using company logo.
Lachlan Voss
Manager/Director
Birch Property Developments
Po Box 4657
Eastbrook Central
Wld
0455 386 218
lachlan@birchpropertydevelopments
eye catching, vibrant colours, professional

```html
<!DOCTYPE html>
<html lang="en">
<head>
<meta charset="utf-8">
<title>Birch Property Developments – Business Card</title>
<link rel="stylesheet" href="https://fonts.googleapis.com/css2?family=Questrial&display=swap">
<style>
  :root {
    --backdrop-light: #4a4a4a;
    --backdrop-dark: #262626;
    --card-white: #ffffff;
    --brand-green-light: #86cf3a;
    --brand-green-deep: #4fb33a;
    --brand-grey: #5d5e60;
    --ink-dark: #111111;
    --ink-light: #ffffff;
  }
  * { margin: 0; padding: 0; box-sizing: border-box; }
  html, body {
    width: 1200px;
    height: 900px;
    overflow: hidden;
  }
  body {
    background: radial-gradient(ellipse at 50% 45%, var(--backdrop-light) 0%, var(--backdrop-dark) 80%);
    font-family: "Questrial", "Century Gothic", sans-serif;
    position: relative;
  }
  .card {
    position: absolute;
    width: 550px;
    height: 315px;
    box-shadow: 0 6px 18px rgba(0, 0, 0, 0.45);
  }
  .card-front {
    left: 325px;
    top: 110px;
    background: var(--card-white);
    display: flex;
    align-items: center;
    justify-content: center;
  }
  .brand-mark {
    display: flex;
    align-items: center;
    gap: 14px;
  }
  .brand-square {
    width: 26px;
    height: 26px;
    background: var(--brand-green-deep);
  }
  .brand-name {
    color: var(--brand-grey);
    font-size: 28px;
    line-height: 1.1;
    text-transform: uppercase;
    letter-spacing: 1px;
  }
  .card-back {
    left: 325px;
    top: 475px;
    background: linear-gradient(120deg, var(--brand-green-light) 0%, var(--brand-green-deep) 100%);
    color: var(--ink-light);
  }
  .card-back .brand-mark {
    position: absolute;
    left: 30px;
    top: 132px;
    width: 190px;
    gap: 10px;
  }
  .card-back .brand-square {
    width: 16px;
    height: 16px;
    flex: none;
    background: var(--ink-light);
  }
  .card-back .brand-name {
    color: var(--ink-light);
    font-size: 15px;
    letter-spacing: 0.5px;
  }
  .divider {
    position: absolute;
    left: 241px;
    top: 42px;
    width: 1.5px;
    height: 226px;
    background: var(--ink-light);
  }
  .contact {
    position: absolute;
    left: 270px;
    top: 54px;
  }
  .contact-name {
    color: var(--ink-dark);
    font-size: 21px;
    line-height: 24px;
    -webkit-text-stroke: 0.4px var(--ink-dark);
  }
  .contact-role {
    font-size: 16px;
    line-height: 20px;
    margin-bottom: 20px;
    -webkit-text-stroke: 0.3px var(--ink-light);
  }
  .contact-address,
  .contact-lines {
    font-size: 12.5px;
    line-height: 15.7px;
    font-style: normal;
    -webkit-text-stroke: 0.2px var(--ink-light);
  }
  .contact-lines { margin-top: 16px; }
</style>
</head>
<body>
  <section class="card card-front" aria-label="Business card front">
    <div class="brand-mark">
      <span class="brand-square" aria-hidden="true"></span>
      <span class="brand-name">Birch Property<br>Developments</span>
    </div>
  </section>

  <section class="card card-back" aria-label="Business card back">
    <div class="brand-mark">
      <span class="brand-square" aria-hidden="true"></span>
      <span class="brand-name">Birch Property Developments</span>
    </div>
    <div class="divider"></div>
    <div class="contact">
      <p class="contact-name">Lachlan Voss</p>
      <p class="contact-role">Manager/Director</p>
      <address class="contact-address">
        Birch Property<br>
        Developments<br>
        Po Box 4657<br>
        Eastbrook Central<br>
        Wld
      </address>
      <p class="contact-lines">
        T: 0455 386 218<br>
        E: lachlan@birchpropertydevelopments
      </p>
    </div>
  </section>
</body>
</html>
```